Stainless Steel Water Bottle Packaging

We need a design for our cylindrical water bottle packaging.

Please see attached template (500ml cola bottle template .ai file) for exact dimensions.

VORO is defined as the elemental forces of nature embodied in an object or person. The design should be eye catching and draw potential clients in. Although its a cylindrical bottle/box, the front which would face the customer when sitting on a shelf should clearly display our logo.

Industry/Entity Type

Steel

Requirements
Must have
• Designed to the specifications of the attached template (see attached)
• Our VORO Logo (see attached) and website www.vorobottle.example(in smaller font) must appear.
• Size of bottle must appear - '17 oz/500 ml'
• These should appear somewhere:
• 'INULATED DOUBLE-WALL STAINLESS STEEL WATER BOTTLE'
• 'VORO Bottles magically keeps drinks cold for up to 24hrs, hot for 12',
• 'BPA Free'
• 'For every VORO bottle purchased, a portion of proceeds will go towards charity. Each of our colour's have been assigned a specific charity. Please visit www.vorobottle.example to find out which charity you helped support!'
• The Top circle - just our Symbol (flame/drop)
• The bottom circle - 'Inc. Designed in Canada made in China' on the outer edge leaving the middle empty for the UPC code.
• Reference website for the bottle case I'm looking for:
• http://shopkorinday.example/t-flow-lagoon-pink-insulated-water-bottle
Nice to have
• illustration of our water bottle shape (see attached) appearing somewhere on the box is something i had in mind but definitely not necessary.

```html
<!DOCTYPE html>
<html lang="en">
<head>
<meta charset="utf-8">
<title>VORO Insulated Bottle Wrap</title>
<link rel="stylesheet" href="https://fonts.googleapis.com/css2?family=Montserrat:wght@500&family=Oswald:wght@500;600&display=swap">
<style>
  :root {
    --backdrop: #ececec;
    --bottle-light: #4fb6e6;
    --bottle-mid: #2f9ad4;
    --bottle-deep: #1f74b4;
    --cap-dark: #3f3f41;
    --cap-light: #6b6c6e;
    --band-silver: #d9dadc;
    --band-shine: #f6f6f6;
    --band-gold: #e2b93b;
    --symbol-gold: #f2bd2c;
    --ink-navy: #1e4f8a;
    --ink-white: #ffffff;
  }
  * { margin: 0; padding: 0; box-sizing: border-box; }
  html, body { width: 668px; height: 1200px; overflow: hidden; }
  body { background: var(--backdrop); position: relative; }

  .bottle { position: absolute; inset: 0; width: 668px; height: 1200px; }

  .wordmark {
    position: absolute; left: 180px; width: 308px; top: 830px;
    text-align: center; color: var(--ink-white);
    font-family: "Montserrat", sans-serif; font-weight: 500;
    font-size: 56px; letter-spacing: 4px; line-height: 1;
  }

  .web-address {
    position: absolute; left: 180px; width: 308px; top: 901px; height: 30px;
    display: flex; align-items: center; justify-content: center;
    color: var(--ink-navy);
    font-family: "Oswald", sans-serif; font-weight: 600;
    font-size: 21px; letter-spacing: 0.2px; white-space: nowrap;
  }

  .tagline, .descriptor, .volume {
    position: absolute; left: 170px; width: 328px; text-align: center;
    color: var(--ink-white); font-family: "Oswald", sans-serif;
    text-transform: uppercase; line-height: 1; white-space: nowrap;
  }
  .tagline { top: 966px; font-size: 9.4px; font-weight: 500; }
  .descriptor { top: 980px; font-size: 13px; font-weight: 500; letter-spacing: 0.2px; }
  .volume { top: 1046px; font-size: 20px; font-weight: 500; letter-spacing: 0.5px; }
</style>
</head>
<body>
  <svg class="bottle" viewBox="0 0 668 1200" aria-hidden="true">
    <defs>
      <linearGradient id="body-fill" x1="0" y1="0" x2="0" y2="1">
        <stop offset="0" stop-color="var(--bottle-light)"/>
        <stop offset="0.55" stop-color="var(--bottle-mid)"/>
        <stop offset="1" stop-color="var(--bottle-deep)"/>
      </linearGradient>
      <linearGradient id="cap-fill" x1="0" y1="0" x2="1" y2="0">
        <stop offset="0" stop-color="var(--cap-dark)"/>
        <stop offset="0.45" stop-color="var(--cap-light)"/>
        <stop offset="1" stop-color="var(--cap-dark)"/>
      </linearGradient>
      <linearGradient id="band-fill" x1="0" y1="0" x2="1" y2="0">
        <stop offset="0" stop-color="var(--band-silver)"/>
        <stop offset="0.5" stop-color="var(--band-shine)"/>
        <stop offset="1" stop-color="var(--band-silver)"/>
      </linearGradient>
    </defs>

    <path class="bottle-body" fill="url(#body-fill)"
      d="M240,170 L428,170 C426,250 430,330 446,400 C464,470 488,520 488,600 L488,1118 Q488,1150 456,1152 L212,1152 Q180,1150 180,1118 L180,600 C180,520 204,470 222,400 C238,330 242,250 240,170 Z"/>

    <g class="bottle-cap">
      <rect x="236" y="28" width="176" height="150" rx="12" fill="url(#cap-fill)"/>
      <rect x="236" y="78" width="176" height="4" fill="var(--cap-dark)"/>
      <rect x="236" y="140" width="176" height="4" fill="var(--cap-dark)"/>
    </g>

    <g class="address-band">
      <rect x="180" y="894" width="308" height="44" fill="url(#band-fill)"/>
      <rect x="180" y="894" width="308" height="4" fill="var(--band-gold)"/>
      <rect x="180" y="934" width="308" height="4" fill="var(--band-gold)"/>
    </g>
  </svg>

  <svg class="brand-symbol" style="position:absolute;left:279px;top:665px" width="110" height="110" viewBox="0 0 110 110" role="img" aria-label="Brand symbol area">
    <circle cx="55" cy="55" r="52" fill="var(--symbol-gold)"/>
  </svg>

  <div class="wordmark">VORO</div>
  <div class="web-address">WWW.VOROBOTTLE.EXAMPLE</div>
  <p class="tagline">VORO Bottles magically keeps drinks cold for up to 24hrs, hot for 12</p>
  <p class="descriptor">Inulated double-wall stainless steel water bottle</p>
  <p class="volume">17 oz/500 ml</p>
</body>
</html>
```